Presentation card Venture KELO - Tech Incubator from Perú

We need a Design to promote the incubator of technology Startups.
We are in Perú, we work with a string tech filter and develop enterprenurship competencies in the Startup team.
The card is to facilitators and staff memebers of VentureKELO.
We want a clear, modern, tech and agile Design.

We work to help New enterprises of technology here in Perú, we expect the candidates have a big competencies to Research and develop technological products.

We work using methodologies from QRB, Folmestry, Brakewell and Harrowgate univeesities. Our book base is the disciplina of enterpreneur.

We work events all year using diferent formats: Brightforge, Vorne price, OPRA Model Competition you can use these logros in your Design.

Set the name, role, email, cell phone number, address.

Example:
// Contact info section
Tobías Quiroveda
Swift Modeling Hub Manager
tobias.quiroveda@kelo-example.pe
(511) 999 000 417

// Address info section
VentureKELO
Technology-based business incubator
Av. Los Cedrales 884, Valdora
Lima - Perú
web: venture-kelo-example.org.pe
email: venture@kelo-example.pe
phone number: (511) 3926508 ext. 4418

// (optional)Lema section
Making happy using technology

// Social network section
facebook: venturekelooficial

Target Market(s)

Enterprenurship, CTO, Investors, Companies interested on open innovation services

Industry/Entity Type

Information Technology

Contact Information for Business Card

Name, Role, Email, Cell phone number

Colors

Designer to choose colors to be used in the design.

Requirements
Must have
• Logo forms and colors
Nice to have
• I add pictures of the leaders of incubator
Should not have
• No vertical designs

```html
<!DOCTYPE html>
<html lang="en">
<head>
<meta charset="utf-8">
<title>Venture KELO – Business Card</title>
<link rel="stylesheet" href="https://fonts.googleapis.com/css2?family=Open+Sans:wght@400;600;700;800&display=swap">
<style>
  :root {
    --stage: #2a2c30;
    --ink: #2b2a2c;
    --magenta: #c1335e;
    --paper: #ffffff;
    --muted: #c9c9cc;
    --font: "Open Sans", Arial, sans-serif;
  }
  * { margin: 0; padding: 0; box-sizing: border-box; }
  html, body { width: 1200px; height: 900px; overflow: hidden; }
  body {
    background: var(--stage);
    font-family: var(--font);
    position: relative;
  }
  .card {
    position: absolute;
    top: 304px;
    width: 510px;
    height: 292px;
    border-radius: 4px;
    overflow: hidden;
    box-shadow: 0 10px 30px rgba(0,0,0,.35);
  }
  .card--front { left: 60px; background: var(--paper); }
  .card--back  { left: 630px; background: var(--ink); }
  .card-shapes { position: absolute; inset: 0; width: 100%; height: 100%; }
  .fill-magenta { fill: var(--magenta); }
  .fill-ink { fill: var(--ink); }
  .fill-paper { fill: var(--paper); }

  .brand {
    position: absolute;
    display: flex;
    align-items: center;
    gap: 8px;
    color: var(--ink);
    font-weight: 800;
    text-transform: uppercase;
    line-height: 1;
    letter-spacing: .5px;
  }
  .brand-square {
    width: 12px; height: 12px;
    background: var(--magenta);
    flex: none;
  }
  .card--front .brand { left: 250px; top: 92px; font-size: 30px; }
  .card--back .brand { left: 378px; top: 112px; font-size: 15px; }
  .brand-name { display: block; }

  .contact {
    position: absolute;
    left: 34px;
    top: 36px;
    color: var(--paper);
  }
  .contact-name { font-size: 18px; font-weight: 700; margin-bottom: 10px; }
  .contact-role { font-size: 10px; font-weight: 600; color: var(--magenta); text-transform: uppercase; letter-spacing: .6px; }
  .contact-line { font-size: 10px; color: var(--muted); line-height: 1.5; }
  .contact-details { margin-top: 22px; }
  .contact-details .contact-line { font-size: 11px; color: var(--paper); line-height: 1.9; }
</style>
</head>
<body>

  <section class="card card--front" aria-label="Card front">
    <svg class="card-shapes" viewBox="0 0 510 292" preserveAspectRatio="none" aria-hidden="true">
      <polygon class="fill-magenta" points="0,0 120,0 300,292 0,292"/>
      <polygon class="fill-ink" points="300,292 238,190 510,128 510,292"/>
    </svg>
    <div class="brand">
      <span class="brand-square"></span>
      <span class="brand-name">Venture KELO</span>
    </div>
  </section>

  <section class="card card--back" aria-label="Card back">
    <svg class="card-shapes" viewBox="0 0 510 292" preserveAspectRatio="none" aria-hidden="true">
      <polygon class="fill-magenta" points="0,172 510,262 510,292 0,292"/>
      <polygon class="fill-paper" points="405,0 510,0 510,262 342,232"/>
    </svg>

    <div class="contact">
      <p class="contact-name">Tobías Quiroveda</p>
      <p class="contact-role">Senior Software</p>
      <p class="contact-line">Development Engineer</p>
      <p class="contact-line">Peru</p>
      <div class="contact-details">
        <p class="contact-line">( 999 ) 999 9999</p>
        <p class="contact-line">mail@kelo-example.pe</p>
      </div>
    </div>

    <div class="brand">
      <span class="brand-square"></span>
      <span class="brand-name">Venture KELO</span>
    </div>
  </section>

</body>
</html>
```